Corvane Project Services - Flyer

Project Breif:
I need a single page A4 Capability Statement, which will be used to market our services to prospective clients, both in print and via email PDF.
It needs to look professional and should incorporate the elements I have uploaded into files, these include:
Capability Statement Text
Corvane Services Company Logo
Additional Logo’s (Tools We Use)
Glimmer Bay Pics can be cut into the page
I have included examples of capability statements as a guide to what i am looking for.
Regards
Derek
Engineering Consulting

```html
<!DOCTYPE html>
<html lang="en">
<head>
<meta charset="utf-8">
<title>Corvane Project Services – Capability Statement</title>
<link href="https://fonts.googleapis.com/css2?family=Montserrat:wght@300;400;500;600;700&display=swap" rel="stylesheet">
<style>
  :root{
    --bg:#e4e4e6;
    --paper:#ffffff;
    --blue:#5b9bd5;
    --blue-dark:#3f82c4;
    --ink:#3a3a3a;
    --grey:#6d6d70;
    --grey-band:#8a8a8d;
    --photo-a:#dfe6ee;
    --photo-b:#b9c9da;
  }
  *{box-sizing:border-box;margin:0;padding:0}
  html,body{width:1200px;height:1200px;overflow:hidden;background:var(--bg);font-family:'Montserrat',sans-serif;color:var(--ink)}
  .sheet{position:absolute;left:200px;top:34px;width:800px;height:1131px;background:var(--paper);overflow:hidden;box-shadow:0 4px 18px rgba(0,0,0,.12)}
  .top-strip{position:absolute;left:0;top:0;width:100%;height:12px;background:var(--blue)}
  .brand{position:absolute;left:40px;top:46px;display:flex;align-items:center;gap:12px}
  .brand-dot{width:44px;height:44px;border-radius:50%;background:var(--blue)}
  .brand-name{font-weight:700;font-size:15px;line-height:1.15;letter-spacing:1px;color:var(--ink);text-transform:uppercase;width:170px}
  .title{position:absolute;right:40px;top:44px;text-align:right}
  .title h1{font-size:34px;font-weight:700;color:var(--grey)}
  .title p{font-size:17px;font-weight:300;color:var(--blue);margin-top:2px}
  .photo{position:absolute;left:0;top:140px;width:100%;height:420px;background:linear-gradient(120deg,var(--photo-a),var(--photo-b) 55%,var(--photo-a));clip-path:polygon(0 0,100% 0,100% 62%,0 100%)}
  .headline{position:absolute;left:40px;top:558px;width:380px;color:var(--blue);font-weight:700;font-size:21px;line-height:1.2;text-transform:uppercase}
  .intro{position:absolute;left:40px;top:668px;width:380px;font-size:13px;line-height:1.42;color:var(--grey)}
  .intro p{margin-bottom:10px}
  .tools{position:absolute;left:40px;top:892px;width:390px}
  .tools h3{font-size:17px;font-weight:700;color:var(--ink);margin-bottom:10px}
  .tool-grid{display:grid;grid-template-columns:repeat(3,auto);gap:9px 22px;justify-content:start}
  .tool{display:flex;align-items:center;gap:6px;font-size:12.5px;font-weight:600;color:var(--grey)}
  .tool i{display:block;width:10px;height:10px;background:var(--blue)}
  .services{position:absolute;left:440px;top:470px;width:320px}
  .services h2{font-size:26px;font-weight:700;color:var(--blue);margin-bottom:6px}
  .svc-bar{background:var(--blue);color:#fff;font-size:14px;font-weight:600;padding:5px 12px;margin:14px 0 8px}
  .svc-list{list-style:none;font-size:12.5px;line-height:1.45;color:var(--grey)}
  .svc-list li{position:relative;padding-left:14px}
  .svc-list li::before{content:"";position:absolute;left:2px;top:7px;width:5px;height:5px;border-radius:50%;background:var(--blue)}
  .footer{position:absolute;left:0;bottom:0;width:100%;height:92px;background:var(--blue);display:flex;align-items:center;justify-content:flex-end;gap:20px;padding-right:28px;color:#fff;font-size:12px;font-weight:600;white-space:nowrap}
  .director{position:absolute;left:0;bottom:0;width:270px;height:130px;background:var(--grey-band);clip-path:polygon(0 0,78% 0,100% 100%,0 100%);color:#fff;padding:58px 0 0 34px}
  .director strong{display:block;font-size:20px;font-weight:700;white-space:nowrap}
  .director span{font-size:13px;font-weight:400}
</style>
</head>
<body>
<div class="sheet">
  <div class="top-strip"></div>

  <div class="brand">
    <div class="brand-dot"></div>
    <div class="brand-name">Corvane Project Services</div>
  </div>

  <div class="title">
    <h1>Capability Statement</h1>
    <p>Corvane Project Services Ltd.</p>
  </div>

  <div class="photo" role="img" aria-label="Photo of colleagues' hands passing documents and reviewing charts at a desk"></div>

  <div class="headline">Corvane Project Services Ltd. is a leading project control consultancy based in Co Cork Ireland</div>

  <div class="intro">
    <p>For over 20 years we have been helping our clients to deliver complex projects and programs throughout mainland Europe.</p>
    <p>We are passionate about empowering organisations to achieve their objectives, on time and on budget.</p>
    <p>We are continually innovating, evolving and learning, utilizing the latest industry tools and techniques to deliver real value to our clients.</p>
    <p>Our goal is to make successful project delivery more achievable and repeatable.</p>
  </div>

  <div class="services">
    <h2>Core Services:</h2>
    <div class="svc-bar">Planning and Scheduling</div>
    <ul class="svc-list">
      <li>Tender Planning</li>
      <li>Interactive Planning / Pull Planning</li>
      <li>EPCMV Planning &amp; Scheduling</li>
      <li>Schedule Earned Value Management</li>
      <li>Independent Schedule Quality Assessment</li>
      <li>Schedule Risk Analysis (Monte Carlo)</li>
      <li>Training</li>
    </ul>
    <div class="svc-bar">Management of Risk</div>
    <ul class="svc-list">
      <li>Risk Management Policies &amp; Procedures</li>
      <li>Risk Management Strategy</li>
      <li>Risk Registers</li>
      <li>Risk Improvement Planning</li>
      <li>Risk Response and Communication</li>
      <li>Risk Management Training</li>
    </ul>
    <div class="svc-bar">Cost Control</div>
    <ul class="svc-list">
      <li>Estimating &amp; Forecasting</li>
      <li>Earned Value Analysis</li>
      <li>Progress Reporting</li>
      <li>Cost Risk Analysis</li>
    </ul>
  </div>

  <div class="tools">
    <h3>Tools We Use:</h3>
    <div class="tool-grid">
      <div class="tool"><i></i>Tarnwell Planner</div>
      <div class="tool"><i></i>Planlane</div>
      <div class="tool"><i></i>Orrel Scheduler</div>
      <div class="tool"><i></i>Brevik</div>
      <div class="tool"><i></i>Quillon</div>
      <div class="tool"><i></i>Riskmark</div>
      <div class="tool"><i></i>Waymark Pro</div>
    </div>
  </div>

  <div class="footer">
    <span>+353 (0)861 447 290</span>
    <span>info@corvaneservices.ie</span>
    <span>www.corvaneservices.ie</span>
  </div>
  <div class="director">
    <strong>Derek Halloran</strong>
    <span>(Managing Director)</span>
  </div>
</div>
</body>
</html>
```